Visitenkarten-Design für Immobilien-Unternehmen
Designer ist sehr bemüht und die Änderungswünsche wurden rasch bearbeitet. Auch wurde im Nachhinein noch mein Wunsch auf Adaptierung zu einem Lackdruck bearbeitet und gesendet. Ich bin mit der Abwicklung vollkommen zufrieden - Vielen Dank
Zielgruppe
Die TOLU Immobilien GmbH ist eine durch Ing. Kilian Frühwald inhabergeführte Gesellschaft, welche sich schwerpunktmäßig mit Immobilieninvestitionen sowie Beteiligungen im Bereich von Wohn- und Gewerbeimmobilien beschäftigt. Das Unternehmen kauft, hält, vermietet und verkauft Liegenschaften aller Art, mit dem Fokus auf Gewerbe- und Wohnimmobilien. Zielgruppe sind Personen, welche Immobilien verkaufen möchten - wir betreiben nur eigene Vermögensverwaltung
siehe: www.tolu-immobilien.at
Aufgabenstellung
schlicht und einfach gehalten - weniger ist mehr - nur die wichtigsten Informationen auf der Visitenkarte.
siehe Homepage: www.tolu-immobilien.at

```html
<!DOCTYPE html>
<html lang="de">
<head>
<meta charset="utf-8">
<title>TOLU Immobilien GmbH – Visitenkarte</title>
<link rel="stylesheet" href="https://fonts.googleapis.com/css2?family=Open+Sans:wght@400;600;700&display=swap">
<style>
  :root {
    --backdrop: #1b1b1d;
    --card: #2f2f31;
    --card-edge: #3a3a3d;
    --ink: #f2f2f2;
    --ink-soft: #c9c9cb;
    --divider: #8c8c90;
    --photo-top: #3b3b3e;
    --photo-bottom: #262628;
  }
  html, body {
    margin: 0;
    width: 1200px;
    height: 898px;
    overflow: hidden;
    background: var(--backdrop);
    font-family: "Open Sans", Arial, sans-serif;
  }
  .stage {
    position: relative;
    width: 1200px;
    height: 898px;
  }
  .card {
    position: absolute;
    top: 299px;
    width: 500px;
    height: 300px;
    border-radius: 24px;
    background: var(--card);
    box-shadow: inset 0 0 0 1px var(--card-edge);
    overflow: hidden;
  }
  .card--front { left: 70px; }
  .card--back { left: 630px; }

  .company-name {
    color: var(--ink);
    font-weight: 600;
    font-size: 22px;
    letter-spacing: 0.5px;
    white-space: nowrap;
  }
  .card--front .company-name {
    position: absolute;
    left: 0;
    width: 262px;
    top: 138px;
    text-align: center;
    font-size: 16px;
    letter-spacing: 0.3px;
  }
  .front-divider {
    position: absolute;
    left: 262px;
    top: 92px;
    width: 2px;
    height: 116px;
    background: var(--divider);
  }
  .contact {
    position: absolute;
    left: 286px;
    top: 96px;
    color: var(--ink);
  }
  .contact__name {
    margin: 0;
    font-weight: 700;
    font-size: 16px;
    letter-spacing: 0.6px;
  }
  .contact__role {
    margin: 2px 0 14px;
    font-size: 12.5px;
    color: var(--ink-soft);
  }
  .contact__list {
    list-style: none;
    margin: 0;
    padding: 0;
    font-size: 12.5px;
  }
  .contact__item {
    display: flex;
    align-items: center;
    gap: 8px;
    margin-bottom: 5px;
  }
  .contact__icon {
    width: 12px;
    height: 12px;
    flex: none;
  }

  .back-photo {
    position: absolute;
    inset: 0;
    background: linear-gradient(160deg, var(--photo-top) 0%, var(--photo-bottom) 70%);
    opacity: 0.85;
  }
  .card--back .company-name {
    position: absolute;
    left: 0;
    right: 0;
    top: 134px;
    text-align: center;
  }
</style>
</head>
<body>
<main class="stage">
  <section class="card card--front" aria-label="Vorderseite">
    <div class="company-name">TOLU Immobilien GmbH</div>
    <div class="front-divider"></div>
    <div class="contact">
      <p class="contact__name">JONAS WEIDLER</p>
      <p class="contact__role">Director</p>
      <ul class="contact__list">
        <li class="contact__item">
          <svg class="contact__icon" viewBox="0 0 12 12" aria-hidden="true"><path d="M2.5 1h2l1 2.5-1.3 1a6 6 0 0 0 3.3 3.3l1-1.3 2.5 1v2a1 1 0 0 1-1 1A9.5 9.5 0 0 1 1.5 2a1 1 0 0 1 1-1z" fill="#f2f2f2"/></svg>
          <span>+43 660 418 27 53</span>
        </li>
        <li class="contact__item">
          <svg class="contact__icon" viewBox="0 0 12 12" aria-hidden="true"><rect x="1" y="2.5" width="10" height="7" rx="1" fill="none" stroke="#f2f2f2" stroke-width="1.2"/><path d="M1.5 3l4.5 3.5L10.5 3" fill="none" stroke="#f2f2f2" stroke-width="1.2"/></svg>
          <span>office@tolu-immobilien.at</span>
        </li>
        <li class="contact__item">
          <svg class="contact__icon" viewBox="0 0 12 12" aria-hidden="true"><circle cx="6" cy="6" r="4.8" fill="none" stroke="#f2f2f2" stroke-width="1.1"/><ellipse cx="6" cy="6" rx="2" ry="4.8" fill="none" stroke="#f2f2f2" stroke-width="1"/><path d="M1.2 6h9.6" stroke="#f2f2f2" stroke-width="1"/></svg>
          <span>www.tolu-immobilien.at</span>
        </li>
      </ul>
    </div>
  </section>

  <section class="card card--back" aria-label="Rückseite">
    <div class="back-photo" role="img" aria-label="Dezentes, dunkles Foto eines Gewerbegebäudes als Hintergrund"></div>
    <div class="company-name">TOLU Immobilien GmbH</div>
  </section>
</main>
</body>
</html>
```